Wine Label Design-Crumbled Ledge Vineyard

Crumbled Ledge Vineyard is in the Barossa Valley in South Australia. The Barossa is recognized as Australia's premier wine region, producing Australia's icon wines and some " new takes on traditional".
This family owned and operated vineyard grows some exceptionally high quality fruit. Most of the fruit is sold and used for some of Australia's most iconic wines. Small quantities are retained by the owners for some wines with very limited availability. (Wines were previously sold as BrellMarston Vineyards Crumbled Ledge ( Shiraz, Cabernet etc).

The wines will in the future be labeled simply ‘Crumbled Ledge Vineyard’. The label will launch this new identity for the single family single vineyard and its high quality wines which are a true expression of the vineyard and derive from the Crumbled Ledge common to this ancient area (800-2000 million years old).
The label should reflect
• Single vineyard, family owned
• vines in very old rock & soils
• High quality & reliability
• Edgy but true, design based thinking (Please note:blue is generally seen as an unacceptable colour for a wine label?? Don’t ask me why)

The wines will be sold mostly direct in Australia ( ie not through retail stores), with limited export to Asia, Scandinavia and Canada.
There are three quality levels and price points in the portfolio
1. Entry level premium for everyday drinking for discriminating drinkers-approx AUD20
2. Super Premium-approx AUD30
3. Limited Release ultlra premium-AUD75-90?
We envisage three variations on the label but with an obvious & common design element. This design element should be able to be used for corporate identification and promotion
The paper stock will be waterproof and self adhesive. Our preference is for designs that engage the user by appealing to both sight and touch. It is preferred that textures be added eg embossing, high build varnish etc-rather than be a facet of the stock itself.
For information on statutory label requirements refer to www.vinoregistry-example.com . In brief
o Front label need not show any mandatory information. However we would prefer Variety, Barossa Valley, Year and alcohol to be shown on the front label
o Back label should show all mandatories and allow for a bar code

Reason: I've had a problem with my wireless broadband account and reception has been intermittent to say the least to the extent that I switched off at the weekend. Just going downtown now for a 'polite discussion' with my service provider.

Reason: I have receiver insufficient designs of quality which we would consider. Too many designs have a "cut and paste" appearance - too few exhibit an original art/design element which truly identifies the product.

Gals & Guys

most of the designs submitted lack punch and originality and are totally unmemorable.
Please-get on Zindle or whatever enter "Wine Label Designs" and do some research b4 u waste your time and mine. Formulaic cut and paste will not win the day. That's not to say that cut and paste can't work-but it must have some originality, impact and command attention. Please surprise me.

Following on from a question from a designer about who is our competition and what we are looking for I sent the following 
"I don't think I can add anything new. Read the brief and comments again and research wine labels on the web. In 30 minutes you'll get a good idea of the creative edgy designs in the industry. There are a plethora of collections. Our competition-anyone with a label. In 2010 there were over 2400 "producers" in other words 2400 producers with at least one label. In fact there are over 25000 Australian wines and then the numerous imported wines.

Target Market(s)

$20 people who budget everyday but have graduated from drinking 'entry level' wines. These people will likely fit into Cat. (b) in the $30 wine

$30 (a) will not over-compromise on some everyday discretionary expenditure.(b) might buy for special occasions

$70-$90 Professional/successful people with high disposable/discretionary income not particularly worried about recession. wine geeks.

Industry/Entity Type

Retail

Requirements
Must have
• identifiable element across range of wines

```html
<!DOCTYPE html>
<html lang="en">
<head>
<meta charset="utf-8">
<title>Crumbled Ledge Vineyard – Label Range</title>
<link href="https://fonts.googleapis.com/css2?family=Cormorant+Garamond:wght@400;500;600&family=Uncial+Antiqua&display=swap" rel="stylesheet">
<style>
  :root {
    --canvas: #f4f2ec;
    --chard-bg: #4b3b2d;
    --chard-edge: #2d231b;
    --chard-ink: #efe6d2;
    --chard-vine: #8c7a55;
    --cab-bg: #8d4220;
    --cab-edge: #571c15;
    --cab-ink: #f6e4c8;
    --cab-vine: #d98a45;
    --shiraz-bg: #ebeadf;
    --shiraz-edge: #a4a39a;
    --shiraz-ink: #4a4a44;
    --shiraz-accent: #4f7a38;
    --shiraz-vine: #d9dca0;
    --mark-chard: #7a1c22;
    --mark-gold: #c9a85a;
  }
  * { box-sizing: border-box; margin: 0; padding: 0; }
  html, body { width: 899px; height: 1200px; overflow: hidden; }
  body {
    background: var(--canvas);
    font-family: "Cormorant Garamond", Georgia, serif;
  }
  .range {
    width: 899px;
    height: 1200px;
    display: flex;
    justify-content: space-between;
    align-items: center;
    padding: 0 14px;
  }
  .wine {
    width: 280px;
    display: flex;
    flex-direction: column;
    align-items: center;
    gap: 150px;
  }
  .brand-mark {
    font-family: "Uncial Antiqua", Georgia, serif;
    font-size: 24px;
    line-height: 1;
    display: flex;
    align-items: center;
    gap: 10px;
  }
  .brand-mark::before {
    content: "";
    width: 16px; height: 16px;
    background: currentColor;
  }
  .wine--chardonnay .brand-mark { color: var(--mark-chard); }
  .wine--cabernet .brand-mark,
  .wine--shiraz .brand-mark { color: var(--mark-gold); }

  .label {
    position: relative;
    width: 280px;
    height: 286px;
    border: 6px solid var(--edge);
    background: var(--bg);
    color: var(--ink);
    overflow: hidden;
  }
  .label::before {
    content: "";
    position: absolute;
    inset: 4px;
    border: 1px solid var(--ink);
    opacity: 0.35;
  }
  .wine--chardonnay .label { --bg: var(--chard-bg); --edge: var(--chard-edge); --ink: var(--chard-ink); --accent: var(--chard-ink); --vine: var(--chard-vine); }
  .wine--cabernet .label { --bg: var(--cab-bg); --edge: var(--cab-edge); --ink: var(--cab-ink); --accent: var(--cab-ink); --vine: var(--cab-vine); }
  .wine--shiraz .label { --bg: var(--shiraz-bg); --edge: var(--shiraz-edge); --ink: var(--shiraz-ink); --accent: var(--shiraz-accent); --vine: var(--shiraz-vine); }

  .label__corner {
    position: absolute;
    width: 9px; height: 9px;
    border: 1px solid var(--ink);
    opacity: 0.6;
  }
  .label__corner--tl { top: 2px; left: 2px; border-right: 0; border-bottom: 0; }
  .label__corner--tr { top: 2px; right: 2px; border-left: 0; border-bottom: 0; }
  .label__corner--bl { bottom: 2px; left: 2px; border-right: 0; border-top: 0; }
  .label__corner--br { bottom: 2px; right: 2px; border-left: 0; border-top: 0; }

  .label__seal {
    position: absolute;
    top: 64px; left: 14px;
    width: 68px; height: 68px;
    border-radius: 50%;
    background: var(--ink);
    opacity: 0.1;
  }
  .label__vine {
    position: absolute;
    left: 110px; top: 120px;
    width: 158px; height: 152px;
    background: linear-gradient(200deg, var(--vine) 0%, transparent 80%);
    clip-path: polygon(20% 8%, 100% 0, 100% 100%, 30% 100%, 10% 70%, 40% 45%);
    opacity: 0.75;
  }
  .label__heading {
    position: absolute;
    top: 22px; left: 0; right: 0;
    text-align: center;
  }
  .label__year { font-size: 13px; font-weight: 600; letter-spacing: 0.5px; line-height: 1.2; }
  .label__region {
    font-family: "Uncial Antiqua", Georgia, serif;
    font-size: 12.5px;
    line-height: 1.25;
    color: var(--accent);
  }
  .label__variety {
    font-size: 14px;
    font-weight: 500;
    line-height: 1.25;
    letter-spacing: 0.3px;
  }
  .label__details {
    margin-top: 10px;
    font-size: 9.5px;
    line-height: 1.3;
    opacity: 0.85;
  }
  .label__rule {
    width: 70px; height: 1px;
    margin: 6px auto 0;
    background: var(--ink);
    opacity: 0.5;
  }
  .label__name {
    position: absolute;
    top: 186px; left: 0; right: 0;
    text-align: center;
    font-family: "Uncial Antiqua", Georgia, serif;
    font-size: 15.5px;
    color: var(--accent);
  }
  .label__legal {
    position: absolute;
    left: 16px; top: 216px;
    display: flex;
    gap: 8px;
    font-size: 7.5px;
    line-height: 1.35;
    opacity: 0.8;
  }
  .label__glass { width: 12px; height: 18px; flex: none; }
</style>
</head>
<body>
<main class="range">

  <article class="wine wine--chardonnay">
    <div class="brand-mark">Crumbled Ledge</div>
    <section class="label">
      <span class="label__corner label__corner--tl"></span><span class="label__corner label__corner--tr"></span>
      <span class="label__corner label__corner--bl"></span><span class="label__corner label__corner--br"></span>
      <div class="label__seal"></div>
      <div class="label__vine" role="img" aria-label="Faded vine and leaf illustration"></div>
      <div class="label__heading">
        <div class="label__year">2012</div>
        <div class="label__region">Barossa Valley</div>
        <div class="label__variety">Chardonnay</div>
        <div class="label__details">Product of Australia<br>750 mL 14.0% vol.</div>
        <div class="label__rule"></div>
      </div>
      <div class="label__name">Crumbled Ledge Vineyard</div>
      <div class="label__legal">
        <svg class="label__glass" viewBox="0 0 12 18"><path d="M2 1h8l-1 7a3 3 0 0 1-6 0z M6 11v5 M3 17h6" fill="none" stroke="currentColor" stroke-width="1"/></svg>
        <div>Lot 4 Ridgefold Lane,<br>Kellerton SA 5300, Australia<br>Preservative (220) added</div>
      </div>
    </section>
  </article>

  <article class="wine wine--cabernet">
    <div class="brand-mark">Crumbled Ledge</div>
    <section class="label">
      <span class="label__corner label__corner--tl"></span><span class="label__corner label__corner--tr"></span>
      <span class="label__corner label__corner--bl"></span><span class="label__corner label__corner--br"></span>
      <div class="label__seal"></div>
      <div class="label__vine" role="img" aria-label="Faded vine and leaf illustration"></div>
      <div class="label__heading">
        <div class="label__year">2012</div>
        <div class="label__region">Barossa Valley</div>
        <div class="label__variety">Cabernet Sauvignon</div>
        <div class="label__details">Product of Australia<br>750 mL 14.0% vol.</div>
        <div class="label__rule"></div>
      </div>
      <div class="label__name">Crumbled Ledge Vineyard</div>
      <div class="label__legal">
        <svg class="label__glass" viewBox="0 0 12 18"><rect x="1" y="2" width="10" height="14" fill="none" stroke="currentColor" stroke-width="1"/></svg>
        <div>Lot 4 Ridgefold Lane,<br>Kellerton SA 5300, Australia<br>Preservative (220) added</div>
      </div>
    </section>
  </article>

  <article class="wine wine--shiraz">
    <div class="brand-mark">Crumbled Ledge</div>
    <section class="label">
      <span class="label__corner label__corner--tl"></span><span class="label__corner label__corner--tr"></span>
      <span class="label__corner label__corner--bl"></span><span class="label__corner label__corner--br"></span>
      <div class="label__seal"></div>
      <div class="label__vine" role="img" aria-label="Faded vine and leaf illustration"></div>
      <div class="label__heading">
        <div class="label__year">2012</div>
        <div class="label__region">Barossa Valley</div>
        <div class="label__variety" style="color: var(--accent)">Shiraz</div>
        <div class="label__details">Product of Australia<br>750 mL 14.0% vol.</div>
        <div class="label__rule"></div>
      </div>
      <div class="label__name">Crumbled Ledge Vineyard</div>
      <div class="label__legal">
        <svg class="label__glass" viewBox="0 0 12 18"><path d="M2 1h8l-1 7a3 3 0 0 1-6 0z M6 11v5 M3 17h6" fill="none" stroke="currentColor" stroke-width="1"/></svg>
        <div>Lot 4 Ridgefold Lane,<br>Kellerton SA 5300, Australia<br>Preservative (220) added</div>
      </div>
    </section>
  </article>

</main>
</body>
</html>
```